Warid Advertising & Publicity business cards

I would like my Company's business card to be designed creatively & profissionally the logo is attached in both Arabic & english and prefer to have my emblem dimmed on the card as well
-Logo ( Arabic & English)
-Name (Arabic & English)
-Title ( Arabic & English)
-----------
-Location
-Landline (icon)
-Mobile phone (icon)
-Email (icon)
-Instagram (icon)
-WhatsApp (icon)

Target Market(s)

Industry/Entity Type

Marketing

Contact Information for Business Card

-Logo ( Arabic & English)
-Name (Arabic & English)
-----------
-Location
-Landline (icon)
-Mobile phone (icon)
-Email (icon)
-Instagram (icon)
-WhatsApp (icon)

Font styles to use
Serif

Requirements
Must have
• all what is mentions in business card details blanked and i will add the data my self
Nice to have
• Dim emblem on my business card both Arabic & english

```html
<!DOCTYPE html>
<html lang="en">
<head>
<meta charset="UTF-8">
<title>Warid Advertising &amp; Publicity — Business Cards</title>
<link rel="stylesheet" href="https://fonts.googleapis.com/css2?family=Lora:wght@400;500&family=Amiri:wght@400;700&display=swap">
<style>
  :root {
    --backdrop: #1b1b1c;
    --card: #303134;
    --card-edge: #3a3b3f;
    --teal: #3fcfc3;
    --ink-light: #eeeeee;
    --ink-soft: #c8c9cb;
    --rule: #bdbdbd;
  }
  * { margin: 0; padding: 0; box-sizing: border-box; }
  html, body {
    width: 1200px;
    height: 900px;
    overflow: hidden;
    background: var(--backdrop);
  }
  .canvas {
    position: relative;
    width: 1200px;
    height: 900px;
    font-family: "Lora", Georgia, serif;
  }
  .card {
    position: absolute;
    left: 331px;
    width: 542px;
    height: 317px;
    border-radius: 18px;
    background: var(--card);
    border: 1px solid var(--card-edge);
  }
  .card--front { top: 119px; }
  .card--back { top: 488px; }

  .brand-mark {
    position: absolute;
    width: 40px;
    height: 40px;
    border-radius: 50%;
    background: var(--teal);
  }
  .brand-rule {
    position: absolute;
    width: 1px;
    background: var(--rule);
  }

  /* Front */
  .card--front .brand-mark { left: 54px; top: 138px; }
  .card--front .brand-rule { left: 110px; top: 126px; height: 62px; }
  .brand-name {
    position: absolute;
    left: 119px;
    top: 124px;
    font-weight: 400;
    font-size: 42px;
    line-height: 1;
    color: var(--ink-light);
  }
  .brand-tagline {
    position: absolute;
    left: 119px;
    top: 172px;
    font-size: 11px;
    color: var(--ink-light);
    white-space: nowrap;
  }
  .person-name {
    position: absolute;
    left: 282px;
    top: 84px;
    font-size: 24px;
    font-weight: 400;
    color: var(--teal);
    white-space: nowrap;
  }
  .person-title {
    position: absolute;
    left: 283px;
    top: 116px;
    font-size: 15px;
    color: var(--ink-soft);
    white-space: nowrap;
  }
  .contact-list {
    position: absolute;
    left: 284px;
    top: 150px;
    list-style: none;
    font-size: 12.5px;
    line-height: 19px;
    color: var(--ink-light);
  }
  .contact-item {
    display: flex;
    align-items: center;
    gap: 8px;
    white-space: nowrap;
  }
  .contact-icon {
    width: 12px;
    height: 12px;
    flex: none;
    fill: none;
    stroke: var(--teal);
    stroke-width: 1.6;
    stroke-linecap: round;
    stroke-linejoin: round;
  }
  .contact-dot {
    width: 10px;
    height: 10px;
    margin: 0 1px;
    flex: none;
    border-radius: 50%;
    background: var(--teal);
  }

  /* Back */
  .card--back .brand-mark { left: 320px; top: 108px; }
  .card--back .brand-rule { left: 289px; top: 88px; height: 80px; }
  .brand-name-ar {
    position: absolute;
    right: 264px;
    top: 76px;
    font-family: "Amiri", "Times New Roman", serif;
    font-weight: 700;
    font-size: 50px;
    line-height: 1;
    color: var(--ink-light);
    direction: rtl;
  }
  .brand-tagline-ar {
    position: absolute;
    right: 264px;
    top: 140px;
    font-family: "Amiri", "Times New Roman", serif;
    font-size: 16px;
    line-height: 1.2;
    color: var(--ink-light);
    direction: rtl;
    white-space: nowrap;
  }
  .person-ar {
    position: absolute;
    left: 0;
    right: 0;
    top: 200px;
    text-align: center;
    font-family: "Amiri", "Times New Roman", serif;
    direction: rtl;
  }
  .person-name-ar {
    font-size: 22px;
    font-weight: 400;
    line-height: 1.3;
    color: var(--teal);
  }
  .person-title-ar {
    font-size: 15px;
    line-height: 1.3;
    color: var(--ink-soft);
  }
</style>
</head>
<body>
<main class="canvas">
  <section class="card card--front" aria-label="Business card front">
    <span class="brand-mark" aria-hidden="true"></span>
    <span class="brand-rule" aria-hidden="true"></span>
    <h1 class="brand-name">Warid</h1>
    <p class="brand-tagline">Advertising and Publicity</p>
    <h2 class="person-name">Omar Haddad</h2>
    <p class="person-title">Managing Director</p>
    <ul class="contact-list">
      <li class="contact-item">
        <svg class="contact-icon" viewBox="0 0 12 12" aria-hidden="true"><path d="M6 11s4-3.6 4-6.5a4 4 0 0 0-8 0C2 7.4 6 11 6 11z"/><circle cx="6" cy="4.5" r="1.3"/></svg>
        Al Sadd Street, Doha
      </li>
      <li class="contact-item">
        <svg class="contact-icon" viewBox="0 0 12 12" aria-hidden="true"><path d="M2.5 1.5h2l1 2.5-1.3 1a6 6 0 0 0 2.8 2.8l1-1.3 2.5 1v2a1 1 0 0 1-1 1A9 9 0 0 1 1.5 2.5a1 1 0 0 1 1-1z"/></svg>
        044-987 654 321
      </li>
      <li class="contact-item">
        <svg class="contact-icon" viewBox="0 0 12 12" aria-hidden="true"><rect x="3" y="1" width="6" height="10" rx="1.2"/><path d="M5.3 9h1.4"/></svg>
        055-123 4567
      </li>
      <li class="contact-item">
        <svg class="contact-icon" viewBox="0 0 12 12" aria-hidden="true"><rect x="1" y="2.5" width="10" height="7" rx="1"/><path d="M1.5 3l4.5 3.5L10.5 3"/></svg>
        info@waridad.com
      </li>
      <li class="contact-item">
        <span class="contact-dot" aria-hidden="true"></span>
        @waridad
      </li>
      <li class="contact-item">
        <span class="contact-dot" aria-hidden="true"></span>
        055-123 4567
      </li>
    </ul>
  </section>

  <section class="card card--back" aria-label="Business card back" lang="ar">
    <h2 class="brand-name-ar">وريد</h2>
    <p class="brand-tagline-ar">للدعاية والإعلان</p>
    <span class="brand-rule" aria-hidden="true"></span>
    <span class="brand-mark" aria-hidden="true"></span>
    <div class="person-ar">
      <p class="person-name-ar">عمر حداد</p>
      <p class="person-title-ar">المدير العام</p>
    </div>
  </section>
</main>
</body>
</html>
```